Cyber Security Consulting Business Flier

Need a single page flier (maybe bi-fold? Looking for your suggestions) to advertise our new cyber security consulting firm to global enterprise clients like Varnel, Pryce-Tollan, Kreft, TU and more. Should include all the information on the attached powerpoint. Please feel free to suggest wording modifications or any aspect of design that could improve our credibility or business development success.

Target market are global enterprise business program managers and executives concerned with managing mobile technology and/or data security. Enterprise IT department managers would also be good targets.

This will be a small-run batch of fliers we will hand out at a few upcoming global technology conferences, typically during the course of 1:1 conversations with prospects and/or partners about our business and the topic of cyber security.

We'd like to stick with colors matching our logo or otherwise complimentary to them, although we're open to color suggestions ... we're a high-end, cyber security consulting firm, so whatever can help convey that message would be great. One designer suggested a stark red and black theme.

Please go look at our (terrible) website for more info. Reading our bios on those pages will help give you a feel for the caliber of work we've done and are seeking with new clients.

Target Market(s)

Industry/Entity Type

Information Technology

Colors

Designer to choose colors to be used in the design.

Requirements
Must have
• Professional look and feel, conveying sense of credibility and senior-level experience. We're literally talking to Varnel as a potential client for our consulting services, so it must appeal to the largest global corporations and government agencies.
Nice to have
• If Peter Walsh had a brochure, it would look like this. We're in a leading-edge technology business, which is unexplored, REALLY cool, complicated, and mission-critical for success.
Should not have
• Cartoons or clutter.

```html
<!DOCTYPE html>
<html lang="en">
<head>
<meta charset="utf-8">
<title>Cortexa – Cyber Security Advisory Flier</title>
<link href="https://fonts.googleapis.com/css2?family=Archivo:wght@400;700;800;900&family=Arimo:wght@400;700&display=swap" rel="stylesheet">
<style>
  :root {
    --backdrop: #e6e7e9;
    --navy: #0d2946;
    --ink: #1f2b3d;
    --white: #ffffff;
    --brand-blue: #3c64b4;
    --teal-deep: #0b3f63;
    --teal: #13809a;
    --glow: #6fd08a;
    --code-dark: #17232d;
    --code-teal: #1e5d72;
    --gold: #e0b323;
  }
  * { box-sizing: border-box; margin: 0; padding: 0; }
  html, body { width: 1200px; height: 1022px; overflow: hidden; }
  body {
    background: var(--backdrop);
    font-family: "Arimo", Arial, sans-serif;
    position: relative;
  }
  .page {
    position: absolute;
    top: 175px;
    width: 520px;
    height: 673px;
    overflow: hidden;
    box-shadow: 0 6px 18px rgba(0,0,0,.18);
  }

  /* ---------- Back page ---------- */
  .page--back { left: 50px; background: var(--navy); }
  .back-visual {
    position: absolute; left: 0; top: 0; width: 100%; height: 250px;
    background:
      radial-gradient(circle at 42% 48%, var(--glow) 0, #2ca58f 14%, transparent 34%),
      linear-gradient(160deg, var(--teal-deep) 0%, var(--teal) 60%, #1aa3b4 100%);
  }
  .back-copy {
    position: absolute; left: 70px; top: 272px; right: 30px;
    color: var(--white);
  }
  .back-copy .lead { font-family: "Archivo", Arial, sans-serif; font-weight: 800; font-size: 17px; line-height: 21px; }
  .back-copy .sub { font-size: 14px; line-height: 18px; margin: 1px 0 8px; }
  .back-copy h3 { font-family: "Archivo", Arial, sans-serif; font-weight: 800; font-size: 17px; line-height: 22px; }
  .back-copy ul { list-style: none; margin: 2px 0 6px 12px; }
  .back-copy li { font-size: 14px; line-height: 22px; }
  .back-copy li::before { content: "•"; margin-right: 8px; font-size: 11px; }
  .back-contact {
    position: absolute; left: 30px; right: 30px; top: 588px;
    border-top: 2px solid var(--white);
    padding-top: 12px; color: var(--white);
    font-family: "Archivo", Arial, sans-serif; font-weight: 800; text-align: center;
  }
  .back-contact .line { font-size: 14px; white-space: nowrap; }
  .back-contact .sep { margin: 0 12px; font-weight: 400; }
  .back-contact .phone { font-size: 15px; margin-top: 6px; }

  /* ---------- Front page ---------- */
  .page--front { left: 630px; background: var(--white); }
  .headline {
    position: absolute; left: 40px; top: 50px;
    font-family: "Archivo", Arial, sans-serif; font-weight: 900;
    font-size: 31px; color: var(--ink); letter-spacing: .5px; line-height: 42px;
  }
  .headline span { display: block; }
  .headline span:nth-child(2) { margin-left: 110px; }
  .headline span:nth-child(3) { margin-left: 220px; }
  .front-visual {
    position: absolute; left: 0; top: 205px; width: 100%; height: 335px;
    background:
      radial-gradient(ellipse 24% 38% at 42% 52%, var(--gold) 0, #b38a1c 60%, transparent 62%),
      linear-gradient(90deg, var(--code-dark) 0%, var(--code-teal) 55%, #2a7f96 100%);
  }
  .logo-box {
    position: absolute; right: 0; top: 470px; width: 205px; height: 170px;
    background: var(--white);
    display: flex; align-items: center; justify-content: center; gap: 10px;
  }
  .logo-box .mark { width: 14px; height: 14px; background: var(--brand-blue); }
  .logo-box .name {
    font-family: "Arimo", Arial, sans-serif; font-weight: 700;
    font-size: 30px; color: var(--brand-blue);
  }
  .front-copy {
    position: absolute; left: 40px; top: 558px; color: var(--ink);
    font-family: "Archivo", Arial, sans-serif; font-weight: 700;
  }
  .front-copy .lead { font-size: 14px; margin-bottom: 6px; }
  .front-copy ul { list-style: none; margin-left: 12px; }
  .front-copy li { font-size: 13px; line-height: 20px; }
  .front-copy li::before { content: "•"; margin-right: 10px; font-size: 10px; }
</style>
</head>
<body>

<section class="page page--back">
  <div class="back-visual" role="img" aria-label="Glowing teal cyber security illustration with a padlock inside a circuit ring and network lines"></div>
  <div class="back-copy">
    <p class="lead">Exploit New Technology Capabilities</p>
    <p class="sub">Protect Your Organization and Products</p>
    <h3>Cyber Security Services:</h3>
    <ul>
      <li>Augmented Reality / Virtual Reality</li>
      <li>Industrial Internet of Things (IoT)</li>
      <li>Wearable Computing</li>
      <li>UAS / Drones</li>
      <li>Unconventional Connected Devices</li>
    </ul>
    <h3>Business Development:</h3>
    <ul>
      <li>Market Analysis and Strategic Planning</li>
      <li>Product Development</li>
      <li>Startup Company Incubation</li>
      <li>Technology Commercialization</li>
    </ul>
  </div>
  <div class="back-contact">
    <p class="line">www.cortexa-advisory.com<span class="sep">|</span>info@cortexa-advisory.com</p>
    <p class="phone">Call: 555.214.0187</p>
  </div>
</section>

<section class="page page--front">
  <h1 class="headline">
    <span>WE INNOVATE...</span>
    <span>WE CREATE...</span>
    <span>WE SECURE...</span>
  </h1>
  <div class="front-visual" role="img" aria-label="Gold shield with a keyhole over a dark teal field of hexadecimal code"></div>
  <div class="logo-box">
    <span class="mark"></span>
    <span class="name">Cortexa</span>
  </div>
  <div class="front-copy">
    <p class="lead">A Global Advisory for Enterprise Clients</p>
    <ul>
      <li>Emerging Technology</li>
      <li>AR/VR/Wearable Solutions</li>
      <li>IoT Device Cyber Security</li>
      <li>Business Innovation</li>
    </ul>
  </div>
</section>

</body>
</html>
```